Expedited Project Word Template, envelopes and powerpoint template
no business card needed already have
n/a
2486 Quill Basin Lane
Ashford, OH 44190
info@tivelmora.com
-uploaded logo needs to have ® symbol placed after the word "growing"
-already have business cards just need word template and letterhead and envelopes
-business focused on renewable energies/fresh produce production/environment, looking for classic corporate look
--trying to limit cost of printing as a start-up, so preference is for white background and then use color to highlight key areas
--powerpoint template looking for title slide, section break slide, main content slide, table slide, and image slide. template should include page numbering and private/confidential in the footer.
Here is how my biz card looks -- please note the tag line on this copy is correct"
"where technology and nature meet"

```html
<!DOCTYPE html>
<html lang="en">
<head>
<meta charset="utf-8">
<title>Tivelmora Fieldworks — Stationery</title>
<link href="https://fonts.googleapis.com/css2?family=Open+Sans:wght@400;600&display=swap" rel="stylesheet">
<style>
  :root {
    --backdrop: #a9a9a9;
    --paper: #ffffff;
    --paper-edge: #d8d8d8;
    --brand-teal: #4cc4e0;
    --ink: #555a5e;
    --ink-soft: #9a9ea2;
    --rule: #c9cdd0;
    --mark-faint: #eef8fb;
  }
  * { box-sizing: border-box; margin: 0; padding: 0; }
  html, body { width: 1200px; height: 768px; overflow: hidden; }
  body {
    background: var(--backdrop);
    font-family: "Open Sans", Arial, sans-serif;
    color: var(--ink);
    position: relative;
  }
  .sheet, .envelope {
    position: absolute;
    background: var(--paper);
    box-shadow: 0 2px 6px rgba(0,0,0,.18);
    overflow: hidden;
  }
  .letterhead { left: 60px; top: 84px; width: 464px; height: 600px; }
  .second-sheet { left: 560px; top: 84px; width: 464px; height: 600px; }
  .envelope { left: 620px; top: 420px; width: 540px; height: 234px; }

  .brand { display: flex; align-items: center; gap: 6px; }
  .brand-dot {
    width: 14px; height: 14px; border-radius: 50%;
    background: var(--brand-teal);
    flex: none;
  }
  .brand-name {
    font-family: "Open Sans", Arial, sans-serif;
    font-weight: 600;
    font-size: 11px;
    color: var(--ink);
    white-space: nowrap;
  }
  .tagline {
    font-size: 6px;
    color: var(--ink-soft);
    margin-top: 3px;
    margin-left: 20px;
    white-space: nowrap;
  }

  .contact { font-size: 7px; line-height: 1.45; color: var(--ink); white-space: nowrap; }
  .contact-row { display: flex; align-items: center; gap: 4px; }
  .contact-row svg { width: 7px; height: 7px; flex: none; }
  .contact-address { margin-bottom: 5px; }

  .letterhead .brand-block { position: absolute; left: 22px; top: 66px; }
  .letterhead .contact { position: absolute; left: 300px; top: 20px; }
  .watermark {
    position: absolute; left: 112px; top: 330px;
    width: 230px; height: 230px; border-radius: 50%;
    background: var(--mark-faint);
  }

  .second-sheet .contact { position: absolute; left: 230px; top: 20px; }
  .notes-box {
    position: absolute; left: 170px; top: 100px;
    width: 220px; height: 118px;
    border: 1px solid var(--rule);
    padding: 18px 14px 0;
  }
  .notes-box span {
    display: block; height: 1px; background: var(--rule);
    margin-bottom: 18px;
  }
  .side-rule {
    position: absolute; left: 135px; top: 0; bottom: 0;
    width: 1px; background: var(--paper-edge);
  }

  .envelope .flap { position: absolute; inset: 0; }
  .envelope .brand-block { position: absolute; left: 24px; top: 92px; }
  .envelope .return-address { position: absolute; left: 24px; top: 176px; font-size: 7px; line-height: 1.45; white-space: nowrap; }
  .envelope .flap-dot {
    position: absolute; left: 440px; top: 28px;
    width: 22px; height: 22px; border-radius: 50%;
    background: var(--brand-teal);
  }
</style>
</head>
<body>

  <section class="sheet second-sheet">
    <div class="side-rule"></div>
    <div class="contact">
      <div class="contact-address">2486 Quill Basin Lane<br>Ashford, OH 44190</div>
      <div class="contact-row">
        <svg viewBox="0 0 10 10"><path d="M2 1h2l1 2.5-1.2.8a5 5 0 0 0 2 2l.8-1.2L9 6v2a1 1 0 0 1-1 1A7 7 0 0 1 1 2a1 1 0 0 1 1-1z" fill="#555a5e"/></svg>
        <span>419.555.0138</span>
      </div>
      <div class="contact-row">
        <svg viewBox="0 0 10 10"><rect x="1" y="2" width="8" height="6" fill="none" stroke="#555a5e"/><path d="M1 2l4 3 4-3" fill="none" stroke="#555a5e"/></svg>
        <span>info@tivelmora.com</span>
      </div>
    </div>
    <div class="notes-box"><span></span><span></span><span></span><span></span><span></span></div>
  </section>

  <section class="sheet letterhead">
    <div class="watermark" role="img" aria-label="Faint brand emblem decoration"></div>
    <div class="contact">
      <div class="contact-address">2486 Quill Basin Lane<br>Ashford, OH 44190</div>
      <div class="contact-row">
        <svg viewBox="0 0 10 10"><path d="M2 1h2l1 2.5-1.2.8a5 5 0 0 0 2 2l.8-1.2L9 6v2a1 1 0 0 1-1 1A7 7 0 0 1 1 2a1 1 0 0 1 1-1z" fill="#555a5e"/></svg>
        <span>419.555.0138</span>
      </div>
      <div class="contact-row">
        <svg viewBox="0 0 10 10"><rect x="1" y="2" width="8" height="6" fill="none" stroke="#555a5e"/><path d="M1 2l4 3 4-3" fill="none" stroke="#555a5e"/></svg>
        <span>info@tivelmora.com</span>
      </div>
    </div>
    <div class="brand-block">
      <div class="brand"><span class="brand-dot"></span><span class="brand-name">Tivelmora Fieldworks</span></div>
      <div class="tagline">where technology and nature meet</div>
    </div>
  </section>

  <section class="envelope">
    <svg class="flap" viewBox="0 0 540 234" preserveAspectRatio="none">
      <path d="M330 0 L540 117 L330 234" fill="none" stroke="#d8d8d8" stroke-width="1"/>
    </svg>
    <div class="flap-dot"></div>
    <div class="brand-block">
      <div class="brand"><span class="brand-dot"></span><span class="brand-name">Tivelmora Fieldworks</span></div>
      <div class="tagline">where technology and nature meet</div>
    </div>
    <div class="return-address">2486 Quill Basin Lane<br>Ashford, OH 44190</div>
  </section>

</body>
</html>
```